Brava Set CEO and Partners Business Card

We need a fresh, fun, simple and clean business card design....we would like a template where we can add a name and title (as well as specific email addresses). We are open to different looks (full logo on one side and a small logo on the company info side, or our logo is in the background but faint on one side but full on the other, or something else cool :-) ). Our colors are in our logo: blue, black and white...however we are not opposed to the use of other colors if it works. We build sets, make props and a host of other things for the film and television industry...our card should reflect creativity, style and professionalism.

A white background would be preferred.

I would like to see an option with Facebook and Instagram icons.

Facebook- facebook.com/bravasetny
Instagram- brava_set

Our website is bravaset-example.com.

Brava Set, Inc.
418 Corvell Avenue, Unit 9
North Hollywood, California 91602
555.210.4873 | tel
555.210.6692 | fax
www.BravaSet-example.com

Sample Name and Title #1:

Peter Halvik
CEO / Co-Owner
555.210.4873 | tel
555.210.6692 | fax
peter@bravaset-example.com
www.BravaSet-example.com

Target Market(s)

Marketing Professionals, Production Designers, Interior Designers, Film Producers, Directors, Art Directors, Event Directors

Industry/Entity Type

Entertainment Industry

Contact Information for Business Card

Peter Halvik
CEO / Co-Owner
555.210.4873 | tel
555.210.6692 | fax
peter@bravaset-example.com
www.BravaSet-example.com

Font styles to use
Sans Serif

Colors
33a6d7
ffffff
1b1b1b

Requirements
Must have
• Logo, All Contact Info, White Background. Symmetry.
Nice to have
• Facebook and Instagram icons with addresses
• Facebook- facebook.com/bravasetny
• Instagram- brava_set

```html
<!DOCTYPE html>
<html lang="en">
<head>
<meta charset="utf-8">
<title>Brava Set — Business Card</title>
<link rel="stylesheet" href="https://fonts.googleapis.com/css2?family=Open+Sans:wght@400;600;700;800&display=swap">
<style>
  :root {
    --brand-blue: #33a6d7;
    --brand-black: #1b1b1b;
    --card-white: #ffffff;
    --backdrop: #e4e5e7;
    --muted: #555555;
    --body-text: #333333;
  }
  * { box-sizing: border-box; margin: 0; padding: 0; }
  html, body { width: 1200px; height: 800px; overflow: hidden; }
  body {
    background: var(--backdrop);
    font-family: "Open Sans", Arial, sans-serif;
    color: var(--brand-black);
    display: flex;
    align-items: center;
    justify-content: center;
    gap: 60px;
  }
  .card {
    position: relative;
    width: 525px;
    height: 300px;
    background: var(--card-white);
    box-shadow: 0 6px 18px rgba(0,0,0,0.12);
    overflow: hidden;
  }
  .card__corner {
    position: absolute;
    inset: 0;
    width: 100%;
    height: 100%;
  }
  .wordmark {
    font-weight: 800;
    color: var(--brand-black);
    letter-spacing: -0.02em;
    line-height: 1;
    white-space: nowrap;
  }

  /* Contact side */
  .contact-card .person {
    position: absolute;
    left: 32px;
    top: 26px;
  }
  .person__name {
    font-size: 19px;
    font-weight: 700;
    line-height: 1.1;
  }
  .person__name .surname { color: var(--brand-blue); }
  .person__title {
    font-size: 11px;
    color: var(--muted);
  }
  .contact-card .wordmark {
    position: absolute;
    left: 32px;
    top: 88px;
    font-size: 50px;
  }
  .contact-details {
    position: absolute;
    left: 32px;
    top: 166px;
    width: 340px;
    font-size: 11.5px;
    color: var(--body-text);
    line-height: 1.55;
  }
  .contact-details .row { display: flex; gap: 16px; white-space: nowrap; }
  .contact-details .label { color: var(--brand-blue); }
  .contact-details .rule {
    border: 0;
    height: 1px;
    background: var(--brand-blue);
    margin: 5px 0 4px;
  }
  .contact-details .address { white-space: nowrap; font-size: 11px; }

  /* Logo side */
  .logo-card .wordmark {
    position: absolute;
    left: 0;
    right: 0;
    top: 92px;
    text-align: center;
    font-size: 64px;
  }
  .socials {
    position: absolute;
    left: 30px;
    bottom: 26px;
    display: flex;
    gap: 14px;
    font-size: 12px;
    color: #444;
  }
  .socials__item { display: flex; align-items: center; gap: 5px; }
  .socials__mark {
    width: 11px;
    height: 11px;
    background: var(--brand-blue);
    border-radius: 2px;
  }
</style>
</head>
<body>

  <article class="card contact-card">
    <div class="person">
      <p class="person__name">Peter <span class="surname">Halvik</span></p>
      <p class="person__title">CEO / Co-Owner</p>
    </div>
    <p class="wordmark">Brava Set</p>
    <div class="contact-details">
      <div class="row"><span><span class="label">T:</span> 555.210.4873</span><span><span class="label">W:</span> www.BravaSet-example.com</span></div>
      <div class="row"><span><span class="label">F:</span> 555.210.6692</span><span><span class="label">E:</span> peter@bravaset-example.com</span></div>
      <hr class="rule">
      <p class="address">418 Corvell Avenue, Unit 9, Westbrook, Oregon 97410</p>
    </div>
    <svg class="card__corner" viewBox="0 0 525 300" preserveAspectRatio="none" aria-hidden="true">
      <polygon points="345,300 525,120 525,300" fill="var(--brand-black)"/>
      <polygon points="365,300 525,140 525,300" fill="var(--brand-blue)"/>
    </svg>
  </article>

  <article class="card logo-card">
    <p class="wordmark">Brava Set</p>
    <div class="socials">
      <span class="socials__item"><span class="socials__mark"></span>bravasetny</span>
      <span class="socials__item"><span class="socials__mark"></span>brava_set</span>
    </div>
    <svg class="card__corner" viewBox="0 0 525 300" preserveAspectRatio="none" aria-hidden="true">
      <polygon points="345,300 525,120 525,300" fill="var(--brand-black)"/>
      <polygon points="365,300 525,140 525,300" fill="var(--brand-blue)"/>
    </svg>
  </article>

</body>
</html>
```